Wordpress website and end user portal (also Wordpress) design

We need a design overhaul for front end website and end user portal, both in Wordpress. See attachment or scope. Designer will provide:
1. Logo design options for us to select
2. Provide stock imagery where needed
3. Design end user portal pages with a slick and innovative look (no functionality, just design).
4. Use screen shots of end user portal after designing to use on website.
Approximately 8-10 website pages in design and design clean up on the end user pages. Will have scope and details in next 48 hours.
Requirements:
1. Wordpress experience
2. Creative mindset
3. Innovative design experience and application
Business Software
5+ page

```html
<!DOCTYPE html>
<html lang="en">
<head>
<meta charset="utf-8">
<title>Harwell Law</title>
<link href="https://fonts.googleapis.com/css2?family=Cinzel:wght@400;700&family=Arimo:wght@400;700&display=swap" rel="stylesheet">
<style>
:root{
  --blue:#0f4fb5;
  --blue-dark:#0b3f99;
  --footer:#0b46ad;
  --green:#1b7a2e;
  --orange:#f5a70d;
  --ink:#333;
  --muted:#777;
  --line:#dcdcdc;
  --gray-bg:#f2f2f2;
  --faq-dark:#6b6b6b;
}
*{margin:0;padding:0;box-sizing:border-box}
html,body{width:1200px;height:3462px;overflow:hidden}
body{position:relative;background:#fff;font-family:"Arimo",Arial,sans-serif;color:var(--ink)}
.abs{position:absolute}

/* header */
.logo{left:88px;top:38px;font-family:"Cinzel",Georgia,serif;font-size:32px;color:var(--blue);letter-spacing:1px}
.btn-top{top:18px;height:36px;width:104px;color:#fff;font-size:13px;font-weight:700;display:flex;align-items:center;justify-content:center;letter-spacing:.5px}
.btn-register{left:897px;background:var(--blue)}
.btn-login{left:1009px;background:var(--green)}
.nav{top:76px;left:0;width:1200px;height:20px;font-family:"Cinzel",Georgia,serif;font-size:13px;color:#333}
.nav span{position:absolute;letter-spacing:.5px;white-space:nowrap}
.nav .active{color:var(--blue);font-weight:700}

/* hero */
.hero-photo{top:110px;left:0;width:1200px;height:680px;background:linear-gradient(135deg,#3a3530 0%,#5b534a 40%,#2d2a27 75%,#1e1c1b 100%)}
.hero-title{left:425px;top:452px;width:350px;height:56px;background:rgba(20,45,90,.75);color:#fff;font-family:"Cinzel",Georgia,serif;font-size:36px;display:flex;align-items:center;justify-content:center;letter-spacing:1px}
.hero-sub{left:256px;top:526px;width:688px;height:56px;background:rgba(40,40,40,.7);color:#fff;font-family:"Cinzel",Georgia,serif;font-size:20px;display:flex;align-items:center;justify-content:center;letter-spacing:1px;white-space:nowrap}
.hero-arrow{top:422px;width:36px;height:36px;border:2px solid #fff;border-radius:50%}

/* section titles */
.section-title{left:0;width:1200px;text-align:center;font-family:"Cinzel",Georgia,serif;color:var(--blue);font-size:30px;letter-spacing:1px;font-weight:400}
.section-text{left:220px;width:760px;text-align:center;font-size:11.5px;line-height:29px;color:var(--muted)}

/* practice cards */
.card{top:1030px;width:491px;height:465px;border:1px solid #e6e6e6;background:#fff}
.card-photo{left:0;top:0;width:100%;height:253px}
.card-title{left:24px;top:282px;font-family:"Cinzel",Georgia,serif;font-size:22px;color:var(--blue);font-weight:400}
.card-text{left:28px;top:328px;width:440px;font-size:11.5px;line-height:29px;color:var(--muted)}
.card-corner{right:0;bottom:0}

/* pricing */
.pricing-bg{left:0;top:1570px;width:1200px;height:946px;background:var(--gray-bg)}
.plan{background:#fff;border:1px solid #e3e3e3}
.plan-head{left:0;top:0;width:100%;height:56px;color:#fff;font-family:"Cinzel",Georgia,serif;font-size:21px;display:flex;align-items:center;justify-content:center;letter-spacing:1px}
.plan-photo{left:0;top:56px;width:100%;height:184px}
.price{width:108px;height:108px;border-radius:50%;background:#fff;border:4px solid #eee;box-shadow:0 2px 6px rgba(0,0,0,.15);display:flex;flex-direction:column;align-items:center;justify-content:center}
.price b{font-family:"Cinzel",Georgia,serif;font-weight:400;font-size:27px}
.price small{font-size:11px;color:#555;letter-spacing:1px}
.feature{left:0;width:100%;height:47px;border-bottom:1px solid #e6e6e6;display:flex;align-items:center;justify-content:center;font-size:11.5px;color:#555;white-space:nowrap}
.plan-btn{height:38px;font-family:"Cinzel",Georgia,serif;font-size:14px;display:flex;align-items:center;justify-content:center;letter-spacing:.5px}

/* faq */
.faq-item{left:312px;width:576px;height:52px;border:1px solid #ccc;border-radius:2px;display:flex;align-items:center;padding-left:46px;font-family:"Cinzel",Georgia,serif;font-size:15px;color:#666;letter-spacing:.5px}
.faq-item svg{position:absolute;left:14px;top:15px}
.faq-open{background:var(--faq-dark);color:#fff;border-color:var(--faq-dark)}
.faq-answer{left:330px;top:2748px;width:540px;font-size:11.5px;line-height:27px;color:var(--muted)}

/* footer */
.footer{left:0;top:3049px;width:1200px;height:413px;background:var(--footer);color:#fff}
.foot-title{top:74px;font-family:"Cinzel",Georgia,serif;font-size:20px;letter-spacing:1px;white-space:nowrap}
.foot-text{font-size:12px;line-height:29px}
.foot-links{font-size:12px;line-height:30px}
.email{left:829px;top:117px;width:263px;height:35px;background:#fff;color:#333;font-size:11px;display:flex;align-items:center;padding-left:14px}
.subscribe{left:829px;top:164px;width:124px;height:32px;background:var(--green);font-size:13px;font-weight:700;display:flex;align-items:center;justify-content:center}
.social{top:230px;width:38px;height:38px;border:2px solid #fff;border-radius:50%}
.copyright{left:0;top:374px;width:1200px;text-align:center;font-size:11px}
</style>
</head>
<body>

<!-- header -->
<div class="abs logo">Harwell Law</div>
<div class="abs btn-top btn-register">REGISTER</div>
<div class="abs btn-top btn-login">LOGIN</div>
<nav class="abs nav">
  <span class="active" style="left:493px">HOME</span>
  <span style="left:590px">FEATURES</span>
  <span style="left:710px">PRICING</span>
  <span style="left:823px">FAQ</span>
  <span style="left:903px">ABOUT US</span>
  <span style="left:1025px">CONTACT US</span>
</nav>

<!-- hero -->
<div class="abs hero-photo" role="img" aria-label="Photo of lawyers in business suits meeting around a table"></div>
<svg class="abs" style="left:0;top:640px" width="1200" height="160" viewBox="0 0 1200 160">
  <polygon points="0,15 600,145 1200,15 1200,160 0,160" fill="#fff"/>
  <polyline points="0,15 600,140 1200,15" fill="none" stroke="#0f4fb5" stroke-width="6"/>
</svg>
<div class="abs hero-title">Harwell Law</div>
<div class="abs hero-sub">Sed ut perspiciatis unde omnis iste natus error sit</div>
<svg class="abs hero-arrow" style="left:42px" viewBox="0 0 36 36"><polyline points="20,11 13,18 20,25" fill="none" stroke="#fff" stroke-width="2.5"/></svg>
<svg class="abs hero-arrow" style="left:1120px" viewBox="0 0 36 36"><polyline points="15,11 22,18 15,25" fill="none" stroke="#fff" stroke-width="2.5"/></svg>

<!-- welcome -->
<h1 class="abs section-title" style="top:836px">Welcome to Harwell Law</h1>
<p class="abs section-text" style="top:897px">Sed ut perspiciatis unde omnis iste natus error sit voluptatem accusantium doloremque laudantium, totam rem aperiam, eaque ipsa quae ab illo inventore veritatis et quasi architecto beatae vitae dicta sunt explicabo. Nemo enim ipsam voluptatem quia voluptas sit aspernatur aut odit aut fugit, sed quia consequuntur magni dolores eos qui ratione voluptatem sequi nesciunt.</p>

<div class="abs card" style="left:88px">
  <div class="abs card-photo" role="img" aria-label="Photo of hands signing a business contract" style="background:linear-gradient(135deg,#e8e4de,#b9b1a6 55%,#6e655c)"></div>
  <h2 class="abs card-title">Business Law</h2>
  <p class="abs card-text">Sed ut perspiciatis unde omnis iste natus error sit voluptatem accusantium doloremque laudantium, totam rem aperiam, eaque ipsa quae ab illo inventore veritatis et quasi architecto beatae vitae dicta sunt explicabo.</p>
  <svg class="abs card-corner" width="68" height="58" viewBox="0 0 68 58"><polygon points="68,0 68,58 0,58" fill="#0f4fb5"/><polyline points="44,34 50,40 44,46" fill="none" stroke="#fff" stroke-width="3"/></svg>
</div>
<div class="abs card" style="left:621px">
  <div class="abs card-photo" role="img" aria-label="Photo of a police officer standing in front of a patrol car at dusk" style="background:linear-gradient(180deg,#6d6a55,#3a3a32 50%,#1c1c1e)"></div>
  <h2 class="abs card-title">Law Enforcement</h2>
  <p class="abs card-text">Sed ut perspiciatis unde omnis iste natus error sit voluptatem accusantium doloremque laudantium, totam rem aperiam, eaque ipsa quae ab illo inventore veritatis et quasi architecto beatae vitae dicta sunt explicabo.</p>
  <svg class="abs card-corner" width="68" height="58" viewBox="0 0 68 58"><polygon points="68,0 68,58 0,58" fill="#0f4fb5"/><polyline points="44,34 50,40 44,46" fill="none" stroke="#fff" stroke-width="3"/></svg>
</div>

<!-- pricing -->
<div class="abs pricing-bg"></div>
<h2 class="abs section-title" style="top:1612px;font-size:34px">Our Pricing</h2>
<p class="abs section-text" style="top:1664px">Sed ut perspiciatis unde omnis iste natus error sit voluptatem accusantium doloremque laudantium, totam rem aperiam, eaque ipsa quae ab</p>

<div class="abs plan" style="left:100px;top:1784px;width:327px;height:639px">
  <div class="abs plan-head" style="background:var(--green)">Small Team</div>
  <div class="abs plan-photo" role="img" aria-label="Photo of a small team meeting in a bright office" style="background:linear-gradient(180deg,#c9ccd0,#8d8f92 60%,#5c5d5f)"></div>
  <div class="abs price" style="left:109px;top:205px"><b style="color:var(--green)">$38</b><small>MONTH</small></div>
  <div class="abs feature" style="top:310px">Aius error sit voluptatem accusantium</div>
  <div class="abs feature" style="top:357px">Sed ut perspiciatis unde omnis iste n</div>
  <div class="abs feature" style="top:404px">atus error sit voluptatem accusantium</div>
  <div class="abs feature" style="top:451px">doloremque laudantium,totam rem</div>
  <div class="abs feature" style="top:498px">aperiam, eaque ipsa quae ab illo</div>
  <div class="abs plan-btn" style="left:47px;top:574px;width:108px;background:var(--green);color:#fff">BUY NOW</div>
  <div class="abs plan-btn" style="left:161px;top:574px;width:118px;border:1px solid var(--green);color:var(--green)">TRY IT FREE</div>
</div>

<div class="abs plan" style="left:436px;top:1722px;width:326px;height:736px">
  <div class="abs plan-head" style="background:var(--blue)">Medium Team</div>
  <div class="abs plan-photo" role="img" aria-label="Photo of a business handshake" style="background:linear-gradient(180deg,#6c7580,#9aa2aa 50%,#4f5660)"></div>
  <div class="abs price" style="left:109px;top:197px"><b style="color:var(--blue)">$55</b><small>MONTH</small></div>
  <div class="abs feature" style="top:310px">Aius error sit voluptatem accusantium</div>
  <div class="abs feature" style="top:357px">Sed ut perspiciatis unde omnis iste n</div>
  <div class="abs feature" style="top:404px">atus error sit voluptatem accusantium</div>
  <div class="abs feature" style="top:451px">doloremque laudantium,totam rem</div>
  <div class="abs feature" style="top:498px">aperiam, eaque ipsa quae ab illo</div>
  <div class="abs feature" style="top:545px">doloremque laudantium,totam rem</div>
  <div class="abs plan-btn" style="left:47px;top:644px;width:108px;background:var(--blue);color:#fff">BUY NOW</div>
  <div class="abs plan-btn" style="left:161px;top:644px;width:118px;border:1px solid var(--blue);color:var(--blue)">TRY IT FREE</div>
</div>

<div class="abs plan" style="left:771px;top:1784px;width:326px;height:639px">
  <div class="abs plan-head" style="background:var(--orange)">Large Team</div>
  <div class="abs plan-photo" role="img" aria-label="Photo of a large team of office workers in a modern lobby" style="background:linear-gradient(180deg,#b6c3d0,#8394a6 55%,#4e5d6d)"></div>
  <div class="abs price" style="left:109px;top:205px"><b style="color:var(--orange)">$115</b><small>MONTH</small></div>
  <div class="abs feature" style="top:310px">Aius error sit voluptatem accusantium</div>
  <div class="abs feature" style="top:357px">Sed ut perspiciatis unde omnis iste n</div>
  <div class="abs feature" style="top:404px">atus error sit voluptatem accusantium</div>
  <div class="abs feature" style="top:451px">doloremque laudantium,totam rem</div>
  <div class="abs feature" style="top:498px">aperiam, eaque ipsa quae ab illo</div>
  <div class="abs plan-btn" style="left:47px;top:574px;width:108px;background:var(--orange);color:#fff">BUY NOW</div>
  <div class="abs plan-btn" style="left:161px;top:574px;width:118px;border:1px solid var(--orange);color:var(--orange)">TRY IT FREE</div>
</div>

<!-- faq -->
<h2 class="abs section-title" style="top:2552px;font-size:34px">Our FAQ's</h2>
<p class="abs section-text" style="top:2606px;left:200px;width:800px">Sed ut perspiciatis unde omnis iste natus error sit voluptatem accusantium doloremque laudantium, totam rem aperiam</p>

<div class="abs faq-item faq-open" style="top:2677px">
  <svg width="24" height="22" viewBox="0 0 24 22"><circle cx="9" cy="9" r="7" fill="none" stroke="#fff" stroke-width="2"/><line x1="14" y1="14" x2="21" y2="20" stroke="#fff" stroke-width="2"/></svg>
  Sed ut perspiciatis unde omnis iste natus?
</div>
<p class="abs faq-answer">Nemo enim ipsam voluptatem quia voluptas sit aspernatur aut odit aut fugit, sed quia consequuntur magni dolores eos qui ratione voluptatem sequi nesciunt.</p>
<div class="abs faq-item" style="top:2818px">
  <svg width="24" height="22" viewBox="0 0 24 22"><circle cx="9" cy="9" r="7" fill="none" stroke="#777" stroke-width="2"/><line x1="14" y1="14" x2="21" y2="20" stroke="#777" stroke-width="2"/></svg>
  Sed ut perspiciatis unde omnis iste natus?
</div>
<div class="abs faq-item" style="top:2878px">
  <svg width="24" height="22" viewBox="0 0 24 22"><circle cx="9" cy="9" r="7" fill="none" stroke="#777" stroke-width="2"/><line x1="14" y1="14" x2="21" y2="20" stroke="#777" stroke-width="2"/></svg>
  Sed ut perspiciatis unde omnis iste natus?
</div>
<div class="abs faq-item" style="top:2938px">
  <svg width="24" height="22" viewBox="0 0 24 22"><circle cx="9" cy="9" r="7" fill="none" stroke="#777" stroke-width="2"/><line x1="14" y1="14" x2="21" y2="20" stroke="#777" stroke-width="2"/></svg>
  Sed ut perspiciatis unde omnis iste natus?
</div>

<!-- footer -->
<footer class="abs footer">
  <div class="abs foot-title" style="left:97px">About Us</div>
  <p class="abs foot-text" style="left:97px;top:128px;width:255px">Sed ut perspiciatis unde omnis iste natus err or sit voluptatem accusantium doloremque lau dantium, totam rem aperiam, eaque ipsa qu ae ab illo inventore veritatis et quasi archite cto beatae vitae dicta sunt explicabo.</p>

  <div class="abs foot-title" style="left:418px">Contact Us</div>
  <div class="abs foot-text" style="left:424px;top:122px;line-height:20px">ADDRESS<br>245 Elm Street #4B<br>Austin 78701 TX</div>
  <div class="abs foot-text" style="left:424px;top:198px;line-height:20px">PHONE<br>512-555-0148</div>
  <div class="abs foot-text" style="left:424px;top:250px;line-height:20px">EMAIL<br>info@harwelllaw.com</div>

  <div class="abs foot-title" style="left:658px">Company</div>
  <div class="abs foot-links" style="left:664px;top:118px">Home<br>Features<br>Pricing<br>FAQ<br>About us<br>Contact us</div>

  <div class="abs foot-title" style="left:829px">Keep in Touch</div>
  <div class="abs email">EMAIL ADDRESS</div>
  <div class="abs subscribe">SUBSCRIBE</div>
  <div class="abs social" style="left:828px"></div>
  <div class="abs social" style="left:870px"></div>
  <div class="abs social" style="left:911px"></div>
  <div class="abs social" style="left:953px"></div>
  <div class="abs social" style="left:996px"></div>

  <div class="abs copyright">© Copyright 2018 &nbsp;Harwell Law. All right reserved</div>
</footer>

</body>
</html>
```